Letterhead for a German Distribution/Manufacturing Company

We need a professional Letterhead in a unique Design.
not to playful.
The Letterhead has to show show that we are a international company with headquater in Germany.
all details like adress, Vat Tax Number, Bank Accout, Eori, email, Company number has to be on the Letterhead.
for example use: VAT TAX DE5140683 Bank Account: Halmer Kreditbank IBAN DE417052381ß240316 Swift: HKRB0513742 EORI 3150827469 Company Number: HRB 58106 Adress: VOLINTRA UG Tannwiesen Strasse 7 Postal Code 09385 City Burgstädt Country: Germany Email: info@volintra-mail.net
the design can be colored but doesnt have to be
Industry/Entity Type
Manufacturing and international distribution
Requirements
Must have
- show that we are a international company with headquater in Germany. our company infos and logo

```html
<!DOCTYPE html>
<html lang="en">
<head>
<meta charset="utf-8">
<title>VOLINTRA UG – Letterhead</title>
<link href="https://fonts.googleapis.com/css2?family=Lato:ital,wght@0,300;0,400;0,700;1,300;1,400&display=swap" rel="stylesheet">
<style>
  :root {
    --backdrop: #d3d9e2;
    --paper: #ffffff;
    --ink-dark: #3a3a3a;
    --ink-body: #6b6b6b;
    --ink-muted: #555555;
    --rule: #4a4a4a;
    --signature-tone: #e4e4e4;
  }
  * { margin: 0; padding: 0; box-sizing: border-box; }
  html, body {
    width: 1200px;
    height: 900px;
    overflow: hidden;
    background: var(--backdrop);
    font-family: "Lato", Arial, sans-serif;
  }
  .letterhead {
    position: absolute;
    left: 296px;
    top: 20px;
    width: 608px;
    height: 860px;
    background: var(--paper);
    box-shadow: 0 6px 24px rgba(40, 50, 70, 0.18);
  }
  .brand {
    position: absolute;
    left: 48px;
    top: 64px;
    display: flex;
    align-items: center;
    gap: 8px;
  }
  .brand-dot {
    width: 22px;
    height: 22px;
    border-radius: 50%;
    background: var(--ink-dark);
  }
  .brand-name {
    font-size: 26px;
    font-weight: 700;
    letter-spacing: 0.5px;
    color: var(--ink-dark);
    line-height: 1;
  }
  .contact {
    position: absolute;
    right: 40px;
    top: 72px;
    display: flex;
    gap: 14px;
    font-size: 7.5px;
    font-style: italic;
    color: var(--ink-muted);
    line-height: 1.6;
  }
  .contact-line { display: flex; align-items: center; gap: 4px; }
  .contact-line svg { width: 7px; height: 7px; flex: none; }
  .salutation {
    position: absolute;
    left: 88px;
    top: 150px;
    font-size: 10.5px;
    font-weight: 300;
    color: var(--ink-body);
  }
  .letter-body {
    position: absolute;
    left: 88px;
    top: 192px;
    width: 440px;
    font-size: 9.6px;
    font-weight: 300;
    font-style: italic;
    line-height: 1.75;
    color: var(--ink-body);
  }
  .letter-body p {
    text-align: justify;
    text-indent: 20px;
    margin-bottom: 12px;
  }
  .signature {
    position: absolute;
    left: 70px;
    top: 500px;
    width: 150px;
    height: 62px;
    background: var(--signature-tone);
    border-radius: 4px;
  }
  .footer-rule {
    position: absolute;
    left: 40px;
    right: 40px;
    top: 790px;
    height: 1px;
    background: var(--rule);
  }
  .footer-details {
    position: absolute;
    left: 40px;
    right: 40px;
    top: 800px;
    font-size: 7.4px;
    color: var(--ink-muted);
    display: flex;
    justify-content: space-between;
    white-space: nowrap;
  }
</style>
</head>
<body>
  <main class="letterhead">
    <header>
      <div class="brand">
        <span class="brand-dot"></span>
        <span class="brand-name">VOLINTRA</span>
      </div>
      <div class="contact">
        <address class="contact-address" style="font-style: italic;">
          Tannwiesen Strasse 7<br>
          09385, Burgstädt Germany
        </address>
        <div class="contact-online">
          <div class="contact-line">
            <svg viewBox="0 0 10 10" aria-hidden="true"><rect x="0.5" y="2" width="9" height="6.5" fill="none" stroke="#555" stroke-width="1"/><path d="M0.5 2 L5 5.5 L9.5 2" fill="none" stroke="#555" stroke-width="1"/></svg>
            <span>info@volintra-mail.net</span>
          </div>
          <div class="contact-line">
            <svg viewBox="0 0 10 10" aria-hidden="true"><circle cx="5" cy="5" r="4.3" fill="none" stroke="#555" stroke-width="1"/><ellipse cx="5" cy="5" rx="1.8" ry="4.3" fill="none" stroke="#555" stroke-width="0.8"/><line x1="0.7" y1="5" x2="9.3" y2="5" stroke="#555" stroke-width="0.8"/></svg>
            <span>volintra-mail.net</span>
          </div>
        </div>
      </div>
    </header>

    <p class="salutation">Dear Malte,</p>

    <section class="letter-body">
      <p>Lorem Ipsum is simply dummy text of the printing and typesetting industry. Lorem Ipsum has been the industry's standard dummy text ever since the 1500s, when an unknown printer took a galley of type and scrambled it to make a type specimen book. It has survived not only five centuries, but also the leap into electronic typesetting, remaining essentially unchanged. It was popularised in the 1960s with the release of Varnel sheets containing Lorem Ipsum passages, and more recently with desktop publishing software like Quillset Composer including versions of Lorem Ipsum.</p>
      <p>Lorem Ipsum is simply dummy text of the printing and typesetting industry. Lorem Ipsum has been the industry's standard dummy text ever since the 1500s, when an unknown printer took a galley of type and scrambled it to make a type specimen book.</p>
      <p>Lorem Ipsum is simply dummy text of the printing and typesetting industry. Lorem Ipsum has been the industry's standard dummy text ever since the 1500s, when an unknown printer took a galley of type and scrambled it to make a type specimen book. It has survived not only five centuries, but also the leap into electronic typesetting, remaining essentially unchanged. It was popularised in the 1960s with the release of Varnel sheets containing Lorem Ipsum passages.</p>
    </section>

    <div class="signature" role="img" aria-label="Handwritten signature of the sender"></div>

    <footer>
      <div class="footer-rule"></div>
      <div class="footer-details">
        <span>VAT TAX DE5140683</span><span>•</span>
        <span>Account: Halmer Kreditbank</span><span>•</span>
        <span>IBAN DE417052381ß240316</span><span>•</span>
        <span>Swift: HKRB0513742</span><span>•</span>
        <span>EORI 3150827469</span><span>•</span>
        <span># HRB 58106</span>
      </div>
    </footer>
  </main>
</body>
</html>
```